Real Estate For Sale Signage

I'm an independent agent in Lismore NSW Australia with high standards and looking for a catching 'For Sale'sign board.
I like classy, elegant, stylish and simple best.
My colours are red, white and black.
I don't have a logo or other font designs I need to stick to. I like the concept of a house or real estate design.
Before I created this project I played around on publisher and created the PDF attached. I'm not sold on it, but I don't mind the way the name has been layed out. Originally I had a white background with black & red font.
Fancy fonts for my name would be nice, but must not be busy.
Updates

Just wanted to advise that I have updated my brief and used the tools available to help get my ideas through.

Thank you for your work and time.

Kind regards
Delphine

Industry/Entity Type

Real Estate

Requirements
Must have
• For Sale
Delphine Marsk Real Estate (must stand out)
0491 572 306 (must stand out)
17 Tindale Crescent East Lismore
www.delphinemarskrealestate.example.au

```html
<!DOCTYPE html>
<html lang="en">
<head>
<meta charset="utf-8">
<title>Delphine Marsk Real Estate — For Sale</title>
<link rel="stylesheet" href="https://fonts.googleapis.com/css2?family=Fredoka:wght@600&family=Bellefair&family=Playfair+Display:ital,wght@1,700;1,900&family=Cormorant+Garamond:wght@600&display=swap">
<style>
  :root {
    --sign-red: #c3302f;
    --house-maroon: #7d1a1a;
    --house-deep: #6a1212;
    --paper: #ffffff;
    --ink-red: #7a1515;
  }
  html, body {
    margin: 0;
    padding: 0;
    overflow: hidden;
    background: var(--paper);
  }
  .sign {
    position: relative;
    width: 900px;
    height: 1200px;
    background: var(--sign-red);
    overflow: hidden;
    color: var(--paper);
  }
  .skyline {
    position: absolute;
    left: 0;
    width: 900px;
  }
  .skyline--top {
    top: 0;
    height: 96px;
    background: linear-gradient(to bottom, var(--sign-red) 0%, var(--house-maroon) 70%, var(--house-deep) 100%);
  }
  .skyline--bottom {
    top: 920px;
    height: 136px;
    background: linear-gradient(to bottom, var(--sign-red) 0%, var(--house-maroon) 60%, var(--house-deep) 100%);
  }
  .headline {
    position: absolute;
    top: 116px;
    left: 0;
    width: 900px;
    margin: 0;
    text-align: center;
    font-family: "Fredoka", sans-serif;
    font-weight: 600;
    font-size: 108px;
    line-height: 1;
    letter-spacing: 2px;
  }
  .with {
    position: absolute;
    top: 240px;
    left: 0;
    width: 900px;
    text-align: center;
    font-family: "Playfair Display", serif;
    font-style: italic;
    font-weight: 900;
    font-size: 42px;
    line-height: 1;
  }
  .agency {
    margin: 0;
    font-family: "Bellefair", serif;
    font-weight: 400;
  }
  .agency__name {
    position: absolute;
    left: 0;
    top: 372px;
    width: 900px;
    text-align: center;
    font-size: 118px;
    line-height: 1;
  }
  .agency__trade {
    position: absolute;
    left: 0;
    top: 570px;
    width: 900px;
    text-align: center;
    font-size: 118px;
    line-height: 1;
  }
  .phone-label {
    position: absolute;
    left: 24px;
    top: 756px;
    font-family: "Playfair Display", serif;
    font-style: italic;
    font-weight: 700;
    font-size: 44px;
    line-height: 1;
  }
  .phone-number {
    position: absolute;
    left: 24px;
    top: 812px;
    font-family: "Fredoka", sans-serif;
    font-weight: 600;
    font-size: 108px;
    line-height: 1;
    letter-spacing: 6px;
    white-space: nowrap;
  }
  .footer {
    position: absolute;
    left: 0;
    top: 1060px;
    width: 900px;
    height: 140px;
    background: var(--paper);
    color: var(--ink-red);
    font-family: "Cormorant Garamond", serif;
    font-weight: 600;
    text-align: center;
  }
  .footer__address {
    position: absolute;
    top: 14px;
    left: 0;
    width: 900px;
    font-size: 44px;
    line-height: 1;
    letter-spacing: 1px;
  }
  .footer__web {
    position: absolute;
    top: 76px;
    left: 0;
    width: 900px;
    font-size: 38px;
    line-height: 1;
  }
</style>
</head>
<body>
  <main class="sign">
    <div class="skyline skyline--top" role="img" aria-label="Row of house silhouettes along the top edge"></div>

    <h1 class="headline">For Sale</h1>
    <div class="with">With</div>

    <h2 class="agency">
      <span class="agency__name">Delphine Marsk</span>
      <span class="agency__trade">Real Estate</span>
    </h2>

    <div class="phone-label">Telphone:</div>
    <div class="phone-number">0491 572 306</div>

    <div class="skyline skyline--bottom" role="img" aria-label="Row of house silhouettes with a rising full moon along the bottom"></div>

    <footer class="footer">
      <div class="footer__address">17 Tindale Crescent East Lismore</div>
      <div class="footer__web">www.delphinemarskrealestate.example.au</div>
    </footer>
  </main>
</body>
</html>
```